Plumbing Product Supply Company Needs Front & Back Cover Design For Instruction Manuals

We need a front and back over design for our instruction manuals that we need to give to clients.

There will also be a picture of the product on the front cover so please use the supplied image as dummy.

it needs to incorporate our logo and branding colours.

We are the industry leader so it needs to be up-market, professional and stand out from the crowd.

Target Market(s)

Plumbing Companies

Industry/Entity Type

Plumbing

Font styles to use
Sans Serif

Colors
abd036
ffffff
000000
eaeaea
cbcbcb

Requirements
Must have
• Front & Back Cover as it will become a booklet.
• The logo is to be on the black background.
Nice to have
• Professional, modern, sleek.
Should not have
• Other colours that what is on the guidelines.

```html
<!DOCTYPE html>
<html lang="en">
<head>
<meta charset="utf-8">
<title>Meridian Relining – Manual Cover Spread</title>
<link href="https://fonts.googleapis.com/css2?family=Roboto:wght@300;400;700&display=swap" rel="stylesheet">
<style>
  :root {
    --lime: #abd036;
    --lime-bright: #9be60f;
    --white: #ffffff;
    --black: #000000;
    --panel-black: #151515;
    --band-grey: #4a5053;
    --pipe-grey: #cbcbcb;
    --page-bg: #eaeceb;
    --label-grey: #6b7478;
  }
  * { box-sizing: border-box; margin: 0; padding: 0; }
  html, body { width: 889px; height: 1200px; overflow: hidden; }
  body {
    background: var(--page-bg);
    font-family: "Roboto", Arial, sans-serif;
    position: relative;
  }
  .spread {
    position: absolute;
    left: 65px; top: 62px;
    width: 759px; height: 537px;
    background: var(--white);
    box-shadow: 0 1px 4px rgba(0,0,0,0.18);
    overflow: hidden;
  }
  .pipes { position: absolute; left: 0; top: 0; }
  .url-band {
    position: absolute; left: 0; top: 294px;
    width: 759px; height: 15px;
    background: var(--band-grey);
    display: flex;
  }
  .url-band span {
    flex: 1; text-align: center;
    color: var(--white);
    font-size: 8.5px; font-weight: 700; letter-spacing: 1.2px;
    line-height: 15px;
  }
  .dark-panel {
    position: absolute; left: 0; top: 315px;
    width: 759px; height: 222px;
    background: radial-gradient(ellipse at 60% 40%, #262626 0%, var(--panel-black) 60%, #0b0b0b 100%);
  }
  .spine {
    position: absolute; left: 377px; top: 150px;
    height: 387px; width: 0;
    border-left: 1px dashed var(--white);
  }
  .tagline {
    position: absolute; left: 402px; top: 66px;
    color: var(--lime-bright);
    line-height: 1;
  }
  .tagline .thin { display: block; font-size: 18px; font-weight: 300; letter-spacing: -0.5px; }
  .tagline .bold { display: block; font-size: 18px; font-weight: 700; margin-top: 2px; }
  .product-photo {
    position: absolute; left: 382px; top: 146px;
    width: 162px; height: 118px;
    background: radial-gradient(ellipse at 50% 55%, #8c8c8c 0%, #bdbdbd 55%, #ffffff 100%);
    border-radius: 10px;
  }
  .back-logo {
    position: absolute; left: 29px; top: 388px;
    color: var(--lime);
    font-size: 13px; font-weight: 700; letter-spacing: 0.5px;
  }
  .back-copy {
    position: absolute; left: 22px; top: 437px;
    width: 112px;
    color: #d8d8d8;
    font-size: 5.3px; line-height: 1.2;
  }
  .back-url {
    position: absolute; left: 22px; top: 504px;
    color: var(--lime);
    font-size: 6px; font-weight: 700;
  }
  .front-logo {
    position: absolute; right: 34px; top: 464px;
    color: var(--lime);
    font-size: 16px; font-weight: 700; letter-spacing: 0.5px;
    text-align: right; line-height: 1.15;
  }
  .side-label {
    position: absolute; top: 620px;
    color: var(--label-grey);
    font-size: 17px; font-weight: 400; letter-spacing: 0.3px;
  }
  .side-label.back { left: 86px; }
  .side-label.front { left: 467px; }
</style>
</head>
<body>
  <section class="spread">
    <svg class="pipes" width="759" height="315" viewBox="0 0 759 315" aria-hidden="true">
      <path d="M584 0 V250 Q584 262 572 270 L560 277 Q545 286 545 300 V315" fill="none" stroke="var(--pipe-grey)" stroke-width="12"/>
      <path d="M0 280 H345 Q369 280 369 256 V152 Q369 127 394 127 H527 Q552 127 552 152 V232 Q552 258 578 258 H759" fill="none" stroke="var(--lime-bright)" stroke-width="12"/>
    </svg>

    <div class="tagline">
      <span class="thin">YOUR PIPELINES</span>
      <span class="bold">SUPPLIES</span>
    </div>

    <div class="product-photo" role="img" aria-label="Product photo: relining kit with tool case, resin tubs, rolls and hose"></div>

    <div class="url-band">
      <span>WWW.MERIDIANRELINING.COM</span>
      <span>WWW.MERIDIANRELINING.COM</span>
    </div>

    <div class="dark-panel"></div>
    <div class="spine"></div>

    <div class="back-logo">MERIDIAN RELINING</div>
    <p class="back-copy">Every component in this kit is tested for long service in lined pipes. Read each step before you begin, keep parts clean and dry, and store resin away from heat. For help with fitting or curing, our team is ready to assist on site or by phone.</p>
    <div class="back-url">WWW.MERIDIANRELINING.COM</div>

    <div class="front-logo">MERIDIAN<br>RELINING SUPPLIES</div>
  </section>

  <div class="side-label back">BACK</div>
  <div class="side-label front">FRONT</div>
</body>
</html>
```